Harbor Wellness Partners -Postcard Design

New Post Card design for a new company based in Florida called "Harbor Wellness Partners". Our website is www.harborwellnesspartners-example.com, our phone is 855-HARBR22 (855-427-2722). We offer a no fee service to help our clients find suitable alcohol/drug abuse/addition treatment so that they can attain LONG-TERM recovery.
The facilities we work with have been hand chosen by us after a rigorous interview process.
We have facilities that use various approaches to suit the needs of the client wanting Long-Term Recovery. Evidence based, 12-step based, christian based, and alternative healing based.
Feel free to add a "tag line" that you think will catch attention. We use..."We help our clients drop anchor in Long-Term Recovery". "Call 1-855-HARBR22 before you have to call 911". "Long-Term recovery is our goal, not temporary sobriety."
We interview the treatment facilities to ensure that top treatment is given to our clients, we don't put there where they will not get the care promised.
Some services we can place for are: Interventions, Detox, Partial Hospitalization Program (PHP), Intensive Out Patient (IOP), Out Patient (OP), Sober Living Communities.
Several facilities with several approaches to treatment & recovery.

I am not a designer, so leaving entire design options open (eg...colors, graphics, fonts, etc....) Postcard size will be either 6 x 4 or 7 x 5.

Target Market(s)

Target Market for these postcards are treatment facilities & potential clients around the country. To give them someone to call for help in placing alcoholics & addicting into treatment facilities with different approaches.

Industry/Entity Type

It Company

Requirements
Must have
• THESE DO NOT HAVE TO BE EXACT WORDING!!
• The facilities we work with have been hand chosen by us after a rigorous interview process.
• Treatment programs: Detox, In-Patient, Partial Hospitalization Program (PHP), Intensive out patient (IOP), Out Patient, Sober Living Communities.
• We have facilities that use various approaches to suit the needs of the client wanting Long-Term Recovery. Evidence based, 12-step based, christian based, and alternative healing based.

```html
<!DOCTYPE html>
<html lang="en">
<head>
<meta charset="utf-8">
<title>Harbor Wellness Partners – Postcard</title>
<link rel="stylesheet" href="https://fonts.googleapis.com/css2?family=Tinos&family=Jost:wght@400;500;700&family=Montserrat:wght@700&display=swap">
<style>
  :root {
    --backdrop: #939497;
    --card-white: #ffffff;
    --ink: #111111;
    --ink-soft: #333333;
    --label: #1a1a1a;
    --photo-light: #d9d2c8;
    --photo-mid: #9a8c7c;
    --photo-denim: #3e5a8a;
    --photo-wood: #6b4a30;
    --overlay-text: #ffffff;
  }
  * { margin: 0; padding: 0; box-sizing: border-box; }
  html, body { width: 854px; height: 1200px; overflow: hidden; background: var(--backdrop); }
  .sheet { position: relative; width: 854px; height: 1200px; }
  .side-label {
    position: absolute; left: 0; width: 854px; text-align: center;
    font: 400 12px "Jost", sans-serif; color: var(--label); letter-spacing: 0.3px;
  }
  .side-label--front { top: 65px; }
  .side-label--back { top: 601px; }
  .postcard { position: absolute; left: 116px; width: 617px; height: 471px; overflow: hidden; }
  .postcard--front { top: 98px; }
  .postcard--back { top: 642px; background: var(--card-white); }
  .postcard svg { display: block; }
  .brand-name { font-family: "Tinos", serif; font-size: 25px; fill: var(--ink); }
  .brand-web { font-family: "Jost", sans-serif; font-size: 9px; fill: var(--ink); }
  .brand-phone { font-family: "Jost", sans-serif; font-weight: 700; font-size: 15px; fill: var(--ink); }
  .brand-phone-alt { font-size: 8px; font-weight: 700; }
  .tagline { font-family: "Montserrat", sans-serif; font-weight: 700; font-size: 13px; fill: var(--overlay-text); }

  .message {
    position: absolute; left: 16px; top: 150px; width: 264px; height: 275px;
    font-family: "Jost", sans-serif; color: var(--ink-soft); font-size: 11.5px; line-height: 1.4;
  }
  .message-lead {
    font-family: "Tinos", serif; font-size: 15px; line-height: 1.25; color: var(--ink);
    margin-bottom: 12px;
  }
  .message-heading {
    font-weight: 700; font-size: 10.5px; letter-spacing: 0.8px; text-transform: uppercase;
    color: var(--ink); margin-bottom: 3px;
  }
  .message-block { margin-bottom: 11px; }
  .message-list { list-style: none; }
  .message-list li { display: inline; }
  .message-list li + li::before { content: " · "; }
  .message-close { font-weight: 500; color: var(--ink); }
</style>
</head>
<body>
<main class="sheet">
  <p class="side-label side-label--front">FRONT</p>

  <section class="postcard postcard--front">
    <svg width="617" height="471" viewBox="0 0 617 471">
      <defs>
        <linearGradient id="front-photo-tone" x1="0" y1="0" x2="1" y2="1">
          <stop offset="0" stop-color="var(--photo-light)"/>
          <stop offset="0.45" stop-color="var(--photo-mid)"/>
          <stop offset="0.75" stop-color="var(--photo-denim)"/>
          <stop offset="1" stop-color="var(--photo-wood)"/>
        </linearGradient>
      </defs>
      <rect class="front-photo" width="617" height="471" fill="url(#front-photo-tone)"
            role="img" aria-label="Photo: a distressed man sitting on the floor holding his head, beside a table with a glass of whiskey and drug paraphernalia"/>
      <g class="brand-block">
        <circle cx="63" cy="77" r="46" fill="var(--ink)"/>
        <line x1="119" y1="13" x2="119" y2="141" stroke="var(--ink)" stroke-width="1.5"/>
        <text class="brand-name" x="131" y="61">HARBOR</text>
        <text class="brand-name" x="131" y="85">WELLNESS</text>
        <text class="brand-name" x="131" y="110">PARTNERS</text>
        <text class="brand-web" x="131" y="121">www.harborwellnesspartners-example.com</text>
        <text class="brand-phone" x="131" y="141">855-HARBR22<tspan class="brand-phone-alt" dx="2">( 427-2722 )</tspan></text>
      </g>
      <text class="tagline" x="279" y="346">Call 1-855-HARBR22 before you have to call 911</text>
    </svg>
  </section>

  <p class="side-label side-label--back">BACK</p>

  <section class="postcard postcard--back">
    <svg width="617" height="471" viewBox="0 0 617 471">
      <g class="brand-block">
        <circle cx="52" cy="63" r="42" fill="var(--ink)"/>
        <line x1="106" y1="4" x2="106" y2="126" stroke="var(--ink)" stroke-width="1.5"/>
        <text class="brand-name" x="115" y="48">HARBOR</text>
        <text class="brand-name" x="115" y="71">WELLNESS</text>
        <text class="brand-name" x="115" y="95">PARTNERS</text>
        <text class="brand-web" x="115" y="106">www.harborwellnesspartners-example.com</text>
        <text class="brand-phone" x="115" y="125">855-HARBR22<tspan class="brand-phone-alt" dx="2">( 427-2722 )</tspan></text>
      </g>
      <line class="message-divider" x1="297" y1="83" x2="297" y2="429" stroke="var(--ink)" stroke-width="1.5"/>
      <rect class="stamp-box" x="494" y="23" width="99" height="99" fill="none" stroke="var(--ink)" stroke-width="1"/>
      <g class="address-lines" stroke="var(--ink)" stroke-width="1.5">
        <line x1="334" y1="229" x2="592" y2="229"/>
        <line x1="334" y1="271" x2="592" y2="271"/>
        <line x1="334" y1="312" x2="592" y2="312"/>
        <line x1="334" y1="354" x2="592" y2="354"/>
      </g>
    </svg>

    <div class="message">
      <p class="message-lead">We help our clients drop anchor in Long-Term Recovery.</p>

      <div class="message-block">
        <h2 class="message-heading">Hand-Chosen Facilities</h2>
        <p>Every facility we work with is hand chosen by us after a rigorous interview process. A no-fee placement service.</p>
      </div>

      <div class="message-block">
        <h2 class="message-heading">Treatment Programs</h2>
        <ul class="message-list">
          <li>Detox</li><li>In-Patient</li><li>Partial Hospitalization (PHP)</li><li>Intensive Out Patient (IOP)</li><li>Out Patient</li><li>Sober Living Communities</li>
        </ul>
      </div>

      <div class="message-block">
        <h2 class="message-heading">Approaches to Recovery</h2>
        <ul class="message-list">
          <li>Evidence based</li><li>12-step based</li><li>Christian based</li><li>Alternative healing based</li>
        </ul>
      </div>

      <p class="message-close">Long-Term recovery is our goal, not temporary sobriety.</p>
    </div>
  </section>
</main>
</body>
</html>
```